Powerpoint template for company specialized in training and coaching

We are a company specialized in training and transforming Leaders of companies in their leadership skills. We also help companies transform their company culture. We look at what is positive and already works for the company. We need a powerpoint template for out training. The look and feel should be professional, warm and personal. We just launched our new website www.bridgeofvalor.nl so you can get a good feel. please also check our social media posts. Usually the diagonal stripes of our logo (the house) comes back here. https://www.linkedin.com/school/18294056/admin/feed/posts/
We need two template. One in our business colors https://bridgeofvalor.nl/zakelijk/ and one in our educational colors. https://bridgeofvalor.nl/opleidingen/.

```html
<!DOCTYPE html>
<html lang="en">
<head>
<meta charset="utf-8">
<title>Bridge of Valor – presentation templates</title>
<link rel="stylesheet" href="https://fonts.googleapis.com/css2?family=Poppins:wght@500;600;700&family=Roboto:wght@400;500&display=swap">
<style>
  :root{
    --canvas:#a3a1a3;
    --ink:#1d1d1b;
    --muted:#6f6f6f;
    --paper:#ffffff;
  }
  .theme-business{--accent:#3d5e60;--accent-soft:#c9d3d3;--stripe:#111111;--icon:#3d5e60;--line-a:#3a7bd5;--line-b:#e0406e;}
  .theme-education{--accent:#b2652e;--accent-soft:#ecd6c6;--stripe:#111111;--icon:#e8a531;--line-a:#7b3fd0;--line-b:#e8b52e;}
  *{box-sizing:border-box;margin:0;padding:0}
  html,body{width:1200px;height:540px;overflow:hidden;background:var(--canvas)}
  body{position:relative;font-family:"Roboto",Arial,sans-serif;color:var(--ink)}
  .slide{position:absolute;width:536px;height:300px;background:var(--paper);overflow:hidden;
    transform-origin:0 0;transform:scale(.4658);box-shadow:0 6px 18px rgba(0,0,0,.35)}
  .decor{position:absolute;inset:0;width:536px;height:300px}
  .brand{position:absolute;top:14px;right:14px;font-family:"Poppins",sans-serif;font-weight:600;font-size:12px;color:var(--accent);display:flex;align-items:center;gap:5px}
  .brand::before{content:"";width:9px;height:9px;background:var(--accent)}
  .page-no{position:absolute;right:7px;bottom:7px;width:14px;height:14px;border-radius:50%;background:#111;color:#fff;font-size:5px;display:flex;align-items:center;justify-content:center}
  .title{position:absolute;left:24px;top:16px;font-family:"Poppins",sans-serif;font-weight:600;font-size:20px;color:var(--ink);white-space:nowrap}
  .title em{font-style:normal;color:var(--accent)}
  .lede{position:absolute;left:24px;top:54px;width:350px;font-size:6.4px;line-height:1.65;color:var(--muted)}
  .photo{position:absolute}
  .hero-photo{left:20px;top:42px;width:496px;height:216px;border-radius:110px;background:linear-gradient(120deg,#3b3028,#7a6452 45%,#a99479 70%,#4d4438)}
  .hero-title{position:absolute;left:0;right:0;top:266px;text-align:center;font-family:"Poppins",sans-serif;font-weight:600;font-size:20px}
  .hero-title em{font-style:normal;color:var(--accent)}
  .team{position:absolute;left:20px;right:20px;top:104px;display:flex;justify-content:space-between}
  .member{width:100px;text-align:center;font-family:"Poppins",sans-serif;font-weight:500;font-size:8.5px}
  .portrait{width:96px;height:96px;border-radius:50%;margin:0 auto 12px}
  .services{position:absolute;left:28px;right:54px;top:105px;display:flex;justify-content:space-between}
  .service{width:126px;text-align:center;font-family:"Poppins",sans-serif;font-weight:500;font-size:15px}
  .arch{width:126px;height:145px;border-radius:63px 63px 0 0;margin-bottom:10px}
  .chart{position:absolute;left:16px;top:88px;width:250px;height:135px}
  .chart-copy{position:absolute;left:293px;top:88px;width:204px;font-size:6.4px;line-height:1.75;color:var(--muted);text-align:justify}
  .cards{position:absolute;left:22px;top:54px;width:460px;display:grid;grid-template-columns:1fr 1fr;gap:18px 14px}
  .card{height:106px;border-radius:52px;background:#fff;box-shadow:0 2px 10px rgba(0,0,0,.12);display:flex;gap:12px;padding:28px 22px 0 24px}
  .card svg{flex:none;width:22px;height:22px;margin-top:1px}
  .card h3{font-family:"Poppins",sans-serif;font-weight:500;font-size:9.5px;margin-bottom:5px}
  .card p{font-size:5.8px;line-height:1.6;color:var(--muted)}
  .closing-photo{inset:0;background:linear-gradient(100deg,#54626c,#9fb0bc 35%,#c9c2b8 60%,#4a4038)}
  .thanks{position:absolute;left:243px;right:0;top:126px;height:70px;border-radius:35px 0 0 35px;background:var(--accent);color:#fff;font-family:"Poppins",sans-serif;font-weight:600;font-size:40px;display:flex;align-items:center;padding-left:24px}
</style>
</head>
<body>

<!-- ===== Business theme ===== -->
<section class="theme-business">
  <article class="slide" style="left:53px;top:51px">
    <div class="photo hero-photo" role="img" aria-label="Photo of a coaching team talking at a table"></div>
    <svg class="decor" viewBox="0 0 536 300"><polygon points="0,0 34,0 0,60" fill="var(--accent)"/><polygon points="0,140 90,0 108,0 0,200" fill="var(--accent)"/><polygon points="120,0 156,0 60,150 24,150" fill="var(--stripe)" opacity=".9"/><polygon points="536,215 536,250 492,300 456,300" fill="var(--accent)"/></svg>
    <div class="brand">Bridge of Valor</div>
    <h1 class="hero-title"><em>Want to make</em> more impact ?</h1>
    <span class="page-no">01</span>
  </article>

  <article class="slide" style="left:311px;top:51px">
    <svg class="decor" viewBox="0 0 536 300"><polygon points="536,210 536,245 490,300 455,300" fill="var(--accent)"/></svg>
    <div class="brand">Bridge of Valor</div>
    <h2 class="title"><em>They will help</em> you further</h2>
    <p class="lede" style="width:380px">If you really want to develop further, if you really want to grow, you need a coach who understands his or her profession down to the last detail. You don't settle for less. Meet our passionate experts.</p>
    <div class="team">
      <div class="member"><div class="portrait" role="img" aria-label="Portrait of Daan Verhoef" style="background:#5d7f86"></div>Daan Verhoef</div>
      <div class="member"><div class="portrait" role="img" aria-label="Portrait of Ilse Brandsma" style="background:#c98a68"></div>Ilse Brandsma</div>
      <div class="member"><div class="portrait" role="img" aria-label="Portrait of Pieter Kamphuis" style="background:#b9738a"></div>Pieter Kamphuis</div>
      <div class="member"><div class="portrait" role="img" aria-label="Portrait of Saskia Vermeulen" style="background:#e6bf61"></div>Saskia Vermeulen</div>
    </div>
    <span class="page-no">04</span>
  </article>

  <article class="slide" style="left:53px;top:199px">
    <svg class="decor" viewBox="0 0 536 300"><polygon points="536,200 536,235 486,300 451,300" fill="var(--accent)"/></svg>
    <div class="brand">Bridge of Valor</div>
    <h2 class="title"><em>About</em> Us</h2>
    <p class="lede">You want to make an impact. Being in charge of your own life. Merge your team into a powerful unit. Or develop yourself professionally in the field of behavioral change and coaching. Growing as a person or organization. The Bridge of Valor coaches will help you further.</p>
    <div class="services">
      <div class="service"><div class="arch" role="img" aria-label="Photo of a personal coaching session" style="background:linear-gradient(#6b8198,#3d3a3c)"></div>Personal</div>
      <div class="service"><div class="arch" role="img" aria-label="Photo of a business team meeting" style="background:linear-gradient(#86907a,#4a3f37)"></div>Commercial</div>
      <div class="service"><div class="arch" role="img" aria-label="Photo of a training workshop" style="background:linear-gradient(#9a8b7d,#5b4d43)"></div>Educations</div>
    </div>
    <span class="page-no">02</span>
  </article>

  <article class="slide" style="left:311px;top:199px">
    <svg class="decor" viewBox="0 0 536 300"><polygon points="0,0 50,0 0,60" fill="var(--accent-soft)" opacity=".7"/><polygon points="536,210 536,245 490,300 455,300" fill="var(--accent)"/></svg>
    <div class="brand">Bridge of Valor</div>
    <h2 class="title"><em>Discover how you</em> make an impact</h2>
    <svg class="chart" viewBox="0 0 250 135" font-family="Roboto" font-size="4" fill="#999">
      <g stroke="#e4e4e4" stroke-width=".5">
        <line x1="20" y1="8" x2="240" y2="8"/><line x1="20" y1="18" x2="240" y2="18"/><line x1="20" y1="28" x2="240" y2="28"/><line x1="20" y1="38" x2="240" y2="38"/><line x1="20" y1="48" x2="240" y2="48"/><line x1="20" y1="58" x2="240" y2="58"/><line x1="20" y1="68" x2="240" y2="68"/><line x1="20" y1="78" x2="240" y2="78"/><line x1="20" y1="88" x2="240" y2="88"/><line x1="20" y1="98" x2="240" y2="98"/><line x1="20" y1="108" x2="240" y2="108"/>
      </g>
      <text x="2" y="10">100%</text><text x="2" y="60">50%</text><text x="2" y="110">0%</text>
      <polyline fill="none" stroke="var(--line-a)" stroke-width="1" points="20,100 38,78 56,92 74,75 92,28 110,45 128,38 146,60 164,60 182,60 200,55 218,30 236,45"/>
      <polyline fill="none" stroke="var(--line-b)" stroke-width="1" points="20,62 38,45 56,72 74,92 92,80 110,58 128,18 146,46 164,84 182,78 200,45 218,45 236,68"/>
      <text x="20" y="120">Jan</text><text x="56" y="120">Mar</text><text x="92" y="120">May</text><text x="128" y="120">Jul</text><text x="164" y="120">Sep</text><text x="200" y="120">Nov</text>
      <circle cx="24" cy="131" r="1.5" fill="var(--line-a)"/><text x="28" y="132.5">Lorem</text>
      <circle cx="60" cy="131" r="1.5" fill="var(--line-b)"/><text x="64" y="132.5">Ipsum</text>
    </svg>
    <p class="chart-copy">Sed ut perspiciatis unde omnis iste natus error sit voluptatem accusantium doloremque laudantium, totam rem aperiam, eaque ipsa quae ab illo inventore veritatis et quasi architecto beatae vitae dicta sunt explicabo. Nemo enim ipsam voluptatem quia voluptas sit aspernatur aut odit aut fugit, sed quia consequuntur magni dolores eos qui ratione voluptatem sequi nesciunt. Neque porro quisquam est, qui dolorem ipsum quia dolor sit amet, consectetur, adipisci velit, sed quia non numquam eius modi tempora incidunt ut labore et dolore magnam aliquam quaerat voluptatem.</p>
    <span class="page-no">05</span>
  </article>

  <article class="slide" style="left:53px;top:348px">
    <svg class="decor" viewBox="0 0 536 300"><polygon points="0,0 50,0 0,60" fill="var(--accent-soft)" opacity=".7"/><polygon points="536,210 536,245 490,300 455,300" fill="var(--accent)"/></svg>
    <div class="brand">Bridge of Valor</div>
    <h2 class="title"><em>Why</em> Us?</h2>
    <div class="cards">
      <div class="card"><svg viewBox="0 0 22 22"><path d="M2 10 11 2 20 10V20H2Z" fill="var(--icon)"/><circle cx="15" cy="15" r="3" fill="#fff"/></svg><div><h3>To the core</h3><p>Your 'home': the core where you and/or your team perform optimally. Where everyone feels good. That's what you look for. And that feels like coming home.</p></div></div>
      <div class="card"><svg viewBox="0 0 22 22"><path d="M2 10 11 2 20 10V20H2Z" fill="var(--icon)"/><path d="M11 17c0-4 3-6 6-6-1 4-3 6-6 6z" fill="#fff"/></svg><div><h3>Growth</h3><p>We set people and organizations in motion. Let them grow. No 'go with the flow', but on your own strength and from your own conscious choices.</p></div></div>
      <div class="card"><svg viewBox="0 0 22 22"><path d="M2 10 11 2 20 10V20H2Z" fill="var(--icon)"/><rect x="11" y="12" width="9" height="7" fill="#fff"/></svg><div><h3>Specific</h3><p>Together we go into depth. We find out what is really going on and tackle the essence. This way you actually give your life a positive spin.</p></div></div>
      <div class="card"><svg viewBox="0 0 22 22"><path d="M2 10 11 2 20 10V20H2Z" fill="var(--icon)"/><circle cx="14" cy="14" r="3.5" fill="none" stroke="#fff" stroke-width="1.5"/></svg><div><h3>Concerned</h3><p>To help you further; that's why we get up in the morning. Driven, astute and committed, we let you discover how you can make an impact.</p></div></div>
    </div>
    <span class="page-no">03</span>
  </article>

  <article class="slide" style="left:311px;top:348px">
    <div class="photo closing-photo" role="img" aria-label="Photo of a smiling coach and a participant in a bright office"></div>
    <svg class="decor" viewBox="0 0 536 300"><polygon points="0,120 100,0 150,0 0,185" fill="var(--accent)" opacity=".35"/><polygon points="0,250 150,60 175,60 20,300 0,300" fill="var(--accent)" opacity=".3"/></svg>
    <div class="brand">Bridge of Valor</div>
    <div class="thanks">Thank You</div>
    <span class="page-no">06</span>
  </article>
</section>

<!-- ===== Education theme ===== -->
<section class="theme-education">
  <article class="slide" style="left:640px;top:51px">
    <div class="photo hero-photo" role="img" aria-label="Photo of a coaching team talking at a table"></div>
    <svg class="decor" viewBox="0 0 536 300"><polygon points="0,0 34,0 0,60" fill="var(--accent)"/><polygon points="0,140 90,0 108,0 0,200" fill="var(--accent)"/><polygon points="120,0 156,0 60,150 24,150" fill="var(--stripe)" opacity=".9"/><polygon points="536,215 536,250 492,300 456,300" fill="var(--accent)"/></svg>
    <div class="brand">Bridge of Valor</div>
    <h1 class="hero-title"><em>Want to make</em> more impact ?</h1>
    <span class="page-no">01</span>
  </article>

  <article class="slide" style="left:898px;top:51px">
    <svg class="decor" viewBox="0 0 536 300"><polygon points="536,210 536,245 490,300 455,300" fill="var(--accent)"/></svg>
    <div class="brand">Bridge of Valor</div>
    <h2 class="title"><em>They will help</em> you further</h2>
    <p class="lede" style="width:380px">If you really want to develop further, if you really want to grow, you need a coach who understands his or her profession down to the last detail. You don't settle for less. Meet our passionate experts.</p>
    <div class="team">
      <div class="member"><div class="portrait" role="img" aria-label="Portrait of Daan Verhoef" style="background:#5d7f86"></div>Daan Verhoef</div>
      <div class="member"><div class="portrait" role="img" aria-label="Portrait of Ilse Brandsma" style="background:#c98a68"></div>Ilse Brandsma</div>
      <div class="member"><div class="portrait" role="img" aria-label="Portrait of Pieter Kamphuis" style="background:#b9738a"></div>Pieter Kamphuis</div>
      <div class="member"><div class="portrait" role="img" aria-label="Portrait of Saskia Vermeulen" style="background:#e6bf61"></div>Saskia Vermeulen</div>
    </div>
    <span class="page-no">04</span>
  </article>

  <article class="slide" style="left:640px;top:199px">
    <svg class="decor" viewBox="0 0 536 300"><polygon points="536,200 536,235 486,300 451,300" fill="var(--accent)"/></svg>
    <div class="brand">Bridge of Valor</div>
    <h2 class="title"><em>About</em> Us</h2>
    <p class="lede">You want to make an impact. Being in charge of your own life. Merge your team into a powerful unit. Or develop yourself professionally in the field of behavioral change and coaching. Growing as a person or organization. The Bridge of Valor coaches will help you further.</p>
    <div class="services">
      <div class="service"><div class="arch" role="img" aria-label="Photo of a personal coaching session" style="background:linear-gradient(#6b8198,#3d3a3c)"></div>Personal</div>
      <div class="service"><div class="arch" role="img" aria-label="Photo of a business team meeting" style="background:linear-gradient(#86907a,#4a3f37)"></div>Commercial</div>
      <div class="service"><div class="arch" role="img" aria-label="Photo of a training workshop" style="background:linear-gradient(#9a8b7d,#5b4d43)"></div>Educations</div>
    </div>
    <span class="page-no">02</span>
  </article>

  <article class="slide" style="left:898px;top:199px">
    <svg class="decor" viewBox="0 0 536 300"><polygon points="0,0 50,0 0,60" fill="var(--accent-soft)" opacity=".7"/><polygon points="536,210 536,245 490,300 455,300" fill="var(--accent)"/></svg>
    <div class="brand">Bridge of Valor</div>
    <h2 class="title"><em>Discover how you</em> make an impact</h2>
    <svg class="chart" viewBox="0 0 250 135" font-family="Roboto" font-size="4" fill="#999">
      <g stroke="#e4e4e4" stroke-width=".5">
        <line x1="20" y1="8" x2="240" y2="8"/><line x1="20" y1="18" x2="240" y2="18"/><line x1="20" y1="28" x2="240" y2="28"/><line x1="20" y1="38" x2="240" y2="38"/><line x1="20" y1="48" x2="240" y2="48"/><line x1="20" y1="58" x2="240" y2="58"/><line x1="20" y1="68" x2="240" y2="68"/><line x1="20" y1="78" x2="240" y2="78"/><line x1="20" y1="88" x2="240" y2="88"/><line x1="20" y1="98" x2="240" y2="98"/><line x1="20" y1="108" x2="240" y2="108"/>
      </g>
      <text x="2" y="10">100%</text><text x="2" y="60">50%</text><text x="2" y="110">0%</text>
      <polyline fill="none" stroke="var(--line-a)" stroke-width="1" points="20,100 38,78 56,92 74,75 92,28 110,45 128,38 146,60 164,60 182,60 200,55 218,30 236,45"/>
      <polyline fill="none" stroke="var(--line-b)" stroke-width="1" points="20,62 38,45 56,72 74,92 92,80 110,58 128,18 146,46 164,84 182,78 200,45 218,45 236,68"/>
      <text x="20" y="120">Jan</text><text x="56" y="120">Mar</text><text x="92" y="120">May</text><text x="128" y="120">Jul</text><text x="164" y="120">Sep</text><text x="200" y="120">Nov</text>
      <circle cx="24" cy="131" r="1.5" fill="var(--line-a)"/><text x="28" y="132.5">Lorem</text>
      <circle cx="60" cy="131" r="1.5" fill="var(--line-b)"/><text x="64" y="132.5">Ipsum</text>
    </svg>
    <p class="chart-copy">Sed ut perspiciatis unde omnis iste natus error sit voluptatem accusantium doloremque laudantium, totam rem aperiam, eaque ipsa quae ab illo inventore veritatis et quasi architecto beatae vitae dicta sunt explicabo. Nemo enim ipsam voluptatem quia voluptas sit aspernatur aut odit aut fugit, sed quia consequuntur magni dolores eos qui ratione voluptatem sequi nesciunt. Neque porro quisquam est, qui dolorem ipsum quia dolor sit amet, consectetur, adipisci velit, sed quia non numquam eius modi tempora incidunt ut labore et dolore magnam aliquam quaerat voluptatem.</p>
    <span class="page-no">05</span>
  </article>

  <article class="slide" style="left:640px;top:348px">
    <svg class="decor" viewBox="0 0 536 300"><polygon points="0,0 50,0 0,60" fill="var(--accent-soft)" opacity=".7"/><polygon points="536,210 536,245 490,300 455,300" fill="var(--accent)"/></svg>
    <div class="brand">Bridge of Valor</div>
    <h2 class="title"><em>Why</em> Us?</h2>
    <div class="cards">
      <div class="card"><svg viewBox="0 0 22 22"><path d="M2 10 11 2 20 10V20H2Z" fill="var(--icon)"/><circle cx="15" cy="15" r="3" fill="#fff"/></svg><div><h3>To the core</h3><p>Your 'home': the core where you and/or your team perform optimally. Where everyone feels good. That's what you look for. And that feels like coming home.</p></div></div>
      <div class="card"><svg viewBox="0 0 22 22"><path d="M2 10 11 2 20 10V20H2Z" fill="var(--icon)"/><path d="M11 17c0-4 3-6 6-6-1 4-3 6-6 6z" fill="#fff"/></svg><div><h3>Growth</h3><p>We set people and organizations in motion. Let them grow. No 'go with the flow', but on your own strength and from your own conscious choices.</p></div></div>
      <div class="card"><svg viewBox="0 0 22 22"><path d="M2 10 11 2 20 10V20H2Z" fill="var(--icon)"/><rect x="11" y="12" width="9" height="7" fill="#fff"/></svg><div><h3>Specific</h3><p>Together we go into depth. We find out what is really going on and tackle the essence. This way you actually give your life a positive spin.</p></div></div>
      <div class="card"><svg viewBox="0 0 22 22"><path d="M2 10 11 2 20 10V20H2Z" fill="var(--icon)"/><circle cx="14" cy="14" r="3.5" fill="none" stroke="#fff" stroke-width="1.5"/></svg><div><h3>Concerned</h3><p>To help you further; that's why we get up in the morning. Driven, astute and committed, we let you discover how you can make an impact.</p></div></div>
    </div>
    <span class="page-no">03</span>
  </article>

  <article class="slide" style="left:898px;top:348px">
    <div class="photo closing-photo" role="img" aria-label="Photo of a smiling coach and a participant in a bright office"></div>
    <svg class="decor" viewBox="0 0 536 300"><polygon points="0,120 100,0 150,0 0,185" fill="var(--accent)" opacity=".35"/><polygon points="0,250 150,60 175,60 20,300 0,300" fill="var(--accent)" opacity=".3"/></svg>
    <div class="brand">Bridge of Valor</div>
    <div class="thanks">Thank You</div>
    <span class="page-no">06</span>
  </article>
</section>

</body>
</html>
```